Standard Company Posters / Notices

We have manufacturing sites, across the sites there are notices that managers put up, sometimes like a poster or door notice. These are not in any standard format or follow any standard layout. We wanted to create a notice template that could be adopted with layout guidance for all our internal notices. Some examples of the notices are below. We have three different sites so we would want to interchange the logo to suit the location, I have also added some images used for our values awards as examples of the look we like.

Target Market(s)

Employees

Industry/Entity Type

Food Manufacturing

Requirements
Must have
• Flexible for the site teams to amend to suit their needs.

```html
<!DOCTYPE html>
<html lang="en">
<head>
<meta charset="utf-8">
<title>Site Notices</title>
<link href="https://fonts.googleapis.com/css2?family=Philosopher:wght@700&family=Marcellus&display=swap" rel="stylesheet">
<style>
  :root {
    --canvas: #bcbec0;
    --gold: #8c6e1f;
    --red: #a61f24;
    --bright-red: #b8262a;
    --green: #1f7a3c;
    --ink: #111111;
    --paper: #f4f4f2;
    --white: #ffffff;
    --brand: #1e6b3a;
    --pattern-tone: rgba(17, 17, 17, 0.38);
  }
  * { margin: 0; padding: 0; box-sizing: border-box; }
  html, body { width: 854px; height: 1200px; overflow: hidden; }
  body { background: var(--canvas); position: relative; color: var(--ink); }

  .notice { position: absolute; left: 56px; width: 742px; height: 524px; }
  .notice--equipment { top: 56px; --band: var(--gold); --corner: var(--bright-red); }
  .notice--access { top: 619px; --band: var(--red); --corner: var(--green); }

  .notice__frame { position: absolute; inset: 0; width: 100%; height: 100%; }
  .band { fill: var(--band); }
  .corner-accent { fill: var(--corner); }
  .pattern-area { fill: var(--pattern-tone); }

  .notice__illustration {
    position: absolute; left: 16px; top: 302px; width: 162px; height: 206px;
    background: linear-gradient(160deg, #c0282c 0%, #8e1b1f 60%, #222 100%);
    border-radius: 8px; opacity: .9;
  }

  .notice__brand {
    position: absolute; left: 522px; top: 388px; width: 160px;
    font-family: "Philosopher", sans-serif; font-weight: 700;
    font-size: 24px; line-height: 1.05; color: var(--brand);
    text-align: center; letter-spacing: .5px;
  }

  .notice__title {
    position: absolute; left: 0; right: 0; top: 84px; text-align: center;
    font-family: "Philosopher", sans-serif; font-weight: 700;
    font-size: 52px; line-height: 1; letter-spacing: 2px; white-space: nowrap;
  }

  .checklist {
    position: absolute; left: 233px; width: 276px; top: 156px; list-style: none;
    font-family: "Marcellus", serif; font-size: 27px; letter-spacing: 2px;
  }
  .checklist__item {
    position: relative; height: 50.5px; line-height: 50.5px; text-align: center; white-space: nowrap;
  }
  .checklist__item:not(:last-child)::after {
    content: ""; position: absolute; left: 0; right: 0; bottom: 0;
    border-bottom: 1px dotted #777;
  }
  .checklist__item:not(:last-child)::before {
    content: ""; position: absolute; left: 58px; right: 58px; bottom: 0;
    border-bottom: 1.5px solid var(--ink);
  }

  .notice__heading {
    position: absolute; left: 0; right: 0; top: 120px; text-align: center;
    font-family: "Philosopher", sans-serif; font-weight: 700;
    font-size: 56px; line-height: 62px; letter-spacing: 2px; white-space: nowrap;
  }
  .notice__subline {
    position: absolute; left: 0; right: 0; top: 330px; text-align: center;
    font-family: "Marcellus", serif; font-size: 31px; line-height: 36px;
  }
</style>
</head>
<body>

  <section class="notice notice--equipment">
    <svg class="notice__frame" viewBox="0 0 842 595" role="img" aria-label="Notice frame with striped and dotted pattern bands">
      <rect class="band" width="842" height="595"/>
      <polygon class="pattern-area" points="455,0 760,0 842,80 842,420 792,380 792,52 500,52"/>
      <polygon class="pattern-area" points="0,200 47,250 47,547 200,547 260,595 0,595"/>
      <polygon points="690,0 842,0 842,170" fill="#111"/>
      <polygon points="0,490 0,595 125,595" fill="var(--white)"/>
      <polygon class="corner-accent" points="0,535 0,595 65,595"/>
      <rect class="pattern-area" x="10" y="16" width="462" height="22"/>
      <rect class="pattern-area" x="375" y="556" width="462" height="22"/>
      <rect x="47" y="52" width="745" height="495" fill="var(--paper)"/>
      <path d="M62 62 H718 M782 125 V535 H62 V62" fill="none" stroke="#111" stroke-width="1.6"/>
      <polygon points="735,25 820,25 820,105" fill="var(--white)" stroke="var(--bright-red)" stroke-width="2"/>
      <circle cx="742" cy="96" r="24" fill="var(--white)" stroke="#111" stroke-width="2"/>
      <circle cx="746" cy="93" r="20" fill="var(--bright-red)"/>
    </svg>
    <div class="notice__illustration" role="img" aria-label="Megaphone illustration with sound lines"></div>
    <div class="notice__brand">HARWELL<br>DAIRY</div>

    <h1 class="notice__title">Block Former Room</h1>
    <ul class="checklist">
      <li class="checklist__item">1 X Dust Pan</li>
      <li class="checklist__item">1 X Brush</li>
      <li class="checklist__item">1 X Long Handle</li>
      <li class="checklist__item">Brush</li>
      <li class="checklist__item">1x Squeegee</li>
    </ul>
  </section>

  <section class="notice notice--access">
    <svg class="notice__frame" viewBox="0 0 842 595" role="img" aria-label="Notice frame with striped and dotted pattern bands">
      <rect class="band" width="842" height="595"/>
      <polygon class="pattern-area" points="455,0 760,0 842,80 842,420 792,380 792,52 500,52"/>
      <polygon class="pattern-area" points="0,200 47,250 47,547 200,547 260,595 0,595"/>
      <polygon points="690,0 842,0 842,170" fill="#111"/>
      <polygon points="0,490 0,595 125,595" fill="var(--white)"/>
      <polygon class="corner-accent" points="0,535 0,595 65,595"/>
      <rect class="pattern-area" x="10" y="16" width="462" height="22"/>
      <rect class="pattern-area" x="375" y="556" width="462" height="22"/>
      <rect x="47" y="52" width="745" height="495" fill="var(--paper)"/>
      <path d="M62 62 H718 M782 125 V535 H62 V62" fill="none" stroke="#111" stroke-width="1.6"/>
      <polygon points="735,25 820,25 820,105" fill="var(--white)" stroke="var(--bright-red)" stroke-width="2"/>
      <circle cx="742" cy="96" r="24" fill="var(--white)" stroke="#111" stroke-width="2"/>
      <circle cx="746" cy="93" r="20" fill="var(--bright-red)"/>
    </svg>
    <div class="notice__illustration" role="img" aria-label="Megaphone illustration with sound lines"></div>
    <div class="notice__brand">HARWELL<br>DAIRY</div>

    <h1 class="notice__heading">FEMALE / VISITORS<br>CHANGING ROOM<br>ONLY</h1>
    <p class="notice__subline">NO MALE DAIRY<br>OPERATIVES</p>
  </section>

</body>
</html>
```